Icon/ Image Creation

Looking for a designer to create 18 images for the following 2 pages

1) http://norvantaweb7.com/qpl/markets-served
2) http://norvantaweb7.com/qpl/solutions
( Accounting & Financials
Distribution
Financial Services
Food and Beverage
Mining-Resource Management
Process Manufacturing
Project Time Accounting
Services Management
Textiles & Fashion

Budgeting & Forecasting
Business Intelligence
Custom Solutions
Customer Relationship Mgmt
Enterprise Resource Planning
Human Resources Management
Small Business Accounting
Asset Management
Web Solutions)

They images do NOT need borders on it and are 250px by 50px high.

Each royalty free stock photo you choose should match the text.

Here is what the images look like from a finished page.
http://norvantaweb7.com/qpl/services
Updates

Project Deadline Extended
Reason: I modified scope of project to make it clearer and easier.

Industry/Entity Type

Business

Requirements
Must have
• I need the Source files so I can edit after project completion. prefer illustrator or Photoshop.

I can supply some source images for the project and have an account with PixoraVault to purchase images if needed on my account.

```html
<!DOCTYPE html>
<html lang="en">
<head>
<meta charset="utf-8">
<title>Industries Served – The Clearpath Company</title>
<link rel="stylesheet" href="https://fonts.googleapis.com/css2?family=Arimo:wght@400;700&family=Tinos:ital,wght@1,400;1,700&display=swap">
<style>
:root{
  --red:#a81e06;
  --red-dark:#7d1402;
  --red-text:#b3290b;
  --grey-text:#4a4a4a;
  --panel-border:#d4d4d4;
  --gold:#d6a35c;
  --teal:#0f7f6a;
  --bg:#ffffff;
}
*{box-sizing:border-box;margin:0;padding:0}
html,body{width:1200px;height:914px;overflow:hidden;background:var(--bg)}
body{font-family:"Arimo",Arial,sans-serif;color:var(--grey-text)}
.page{position:absolute;left:0;top:0;width:940px;height:716px;overflow:hidden;transform:scale(1.2766);transform-origin:0 0;background:linear-gradient(#fff 0,#f3f3f3 130px,#fff 160px)}

/* utility bar */
.utility{position:absolute;left:545px;top:0;width:361px;height:27px;border-radius:0 0 12px 12px;background:linear-gradient(#d8d8d8,#bdbdbd);display:flex;align-items:center;padding-left:26px;font-size:12px;color:#444}
.utility .lock{width:14px;height:14px;margin-right:10px}
.utility .divider{width:1px;height:16px;background:#999;margin:0 16px 0 24px}
.search{width:136px;height:19px;background:#8f8f8f;color:#d6d6d6;font-size:12px;padding:2px 6px;border:1px solid #777}
.search-btn{width:17px;height:17px;border-radius:50%;background:#f2f2f2;margin-left:9px;display:flex;align-items:center;justify-content:center}

/* brand */
.brand{position:absolute;left:17px;top:38px}
.brand .mark{width:40px;height:40px;border-radius:50%;background:#f26a1b;margin-left:52px}
.brand .name{font-size:12.5px;font-weight:700;letter-spacing:1.2px;color:#333;margin-top:4px}
.brand .tag{font-size:9px;color:#333;margin-left:98px;margin-top:1px}
.store{position:absolute;left:545px;top:60px;font-family:"Tinos",serif;font-style:italic;font-weight:700;font-size:18px;color:#8a8a8a;line-height:22px}
.store .store-name{color:var(--teal);font-size:28px}
.store .line2{margin-left:45px;font-style:normal}

/* nav */
.nav{position:absolute;left:31px;top:135px;display:flex;gap:3px}
.nav a{height:25px;display:flex;align-items:center;justify-content:center;font-size:12px;color:#555;text-decoration:none;background:linear-gradient(#fdfdfd,#e4e4e4);border:1px solid #d3d3d3;border-bottom:none}

/* hero band */
.hero{position:absolute;left:0;top:160px;width:940px;height:118px;background:linear-gradient(var(--red-dark),var(--red) 40%,var(--red))}
.hero-panel{position:absolute;left:22px;top:18px;width:896px;height:86px;background:linear-gradient(#fff,#eaeaea);border:2px solid #f0f0f0}
.hero-photo{position:absolute;left:0;top:0;width:252px;height:82px;background:linear-gradient(135deg,#4f7aa8,#9ab6cf 55%,#c98a3c)}
.hero-title{position:absolute;left:285px;top:4px;font-size:29px;font-weight:400;color:var(--red-text)}
.hero-sub{position:absolute;left:285px;top:47px;font-size:16.5px;color:var(--red-text)}

/* sidebar */
.sidebar{position:absolute;left:15px;top:308px;width:211px;height:410px;border:1px solid var(--panel-border);border-bottom:none;background:#fff}
.side-menu{position:absolute;left:8px;top:5px;width:193px;border:2px solid var(--gold);list-style:none}
.side-menu li{height:30px;display:flex;align-items:center;font-size:12px;color:#333;background:linear-gradient(#fafafa,#d8d8d8);border-left:3px solid var(--red-dark);border-bottom:1px solid #fff;padding-left:13px;white-space:nowrap}
.side-menu li:first-child{border-top:2px solid var(--red-dark)}
.arrow{width:21px;height:21px;margin-right:9px;flex:none}
.side-link{position:absolute;left:8px;width:193px;height:58px;border:2px solid var(--gold);border-top:3px solid var(--red-dark);background:linear-gradient(#fdfdfd,#dcdcdc);display:flex;align-items:center;font-size:12.5px;font-weight:700;color:#222}
.side-link .icon{width:44px;height:30px;margin:0 20px 0 14px;border-radius:3px}
.remote{top:296px}
.remote .icon{background:linear-gradient(#cfcfcf,#8a8a8a)}
.cases{top:356px}
.cases .icon{background:linear-gradient(#666,#222)}

/* content */
.content-title{position:absolute;left:244px;top:323px;font-size:17.5px;font-weight:700;color:#555}
.card{position:absolute;width:332px;height:148px;border:1px solid var(--panel-border);border-radius:4px;background:linear-gradient(#fff,#f4f4f4);box-shadow:0 1px 2px rgba(0,0,0,.12)}
.card h3{position:absolute;left:15px;top:11px;font-size:17.5px;font-weight:400;color:var(--red-text);letter-spacing:.3px}
.card p{position:absolute;left:15px;top:42px;width:178px;font-size:11.5px;line-height:16px;color:#444;letter-spacing:.3px}
.card .thumb{position:absolute;right:14px;top:38px;width:118px;height:88px;border-radius:6px}
.c1{left:242px;top:358px}.c2{left:582px;top:358px}.c3{left:242px;top:515px}.c4{left:582px;top:515px}
.c1 .thumb{background:linear-gradient(135deg,#c9b89a,#8f9d86 50%,#e07a34)}
.c2 .thumb{background:linear-gradient(135deg,#d22a1c,#b8844c 60%,#8a5a2c)}
.c3 .thumb{background:linear-gradient(135deg,#a9c39a,#5f8c53 50%,#e6c45a)}
.c4 .thumb{background:linear-gradient(135deg,#cfe3f3,#d4352b 45%,#c99a52)}
</style>
</head>
<body>
<div class="page">

  <div class="utility">
    <svg class="lock" viewBox="0 0 14 14"><rect x="2" y="6" width="10" height="8" rx="1" fill="#555"/><path d="M4 6V4a3 3 0 0 1 6 0v2" fill="none" stroke="#555" stroke-width="1.6"/></svg>
    <span>Secure Site Login</span>
    <span class="divider"></span>
    <div class="search">search...</div>
    <div class="search-btn"><svg width="10" height="10" viewBox="0 0 10 10"><circle cx="4" cy="4" r="3" fill="none" stroke="#444" stroke-width="1.4"/><path d="M6.2 6.2 9 9" stroke="#444" stroke-width="1.6"/></svg></div>
  </div>

  <div class="brand">
    <div class="mark"></div>
    <div class="name">THE CLEARPATH COMPANY</div>
    <div class="tag">Ledgerly® Solutions. Delivered</div>
  </div>

  <div class="store">
    Your <span class="store-name">Ledgerly</span> Store... for accounting &amp;<br>
    <span class="line2">business management software.</span>
  </div>

  <nav class="nav">
    <a style="width:65px">HOME</a>
    <a style="width:92px">ABOUT US</a>
    <a style="width:103px">INDUSTRIES</a>
    <a style="width:99px">SOLUTIONS</a>
    <a style="width:89px">SERVICES</a>
    <a style="width:97px">PRODUCTS</a>
    <a style="width:133px">INDUSTRY NEWS</a>
    <a style="width:106px">CONTACT US</a>
  </nav>

  <section class="hero">
    <div class="hero-panel">
      <div class="hero-photo" role="img" aria-label="Photo of two construction workers in hard hats and safety vests at a steel-frame building site"></div>
      <h1 class="hero-title">Industries Served</h1>
      <p class="hero-sub">We specialize. Because you can't be all things to all people.</p>
    </div>
  </section>

  <aside class="sidebar">
    <ul class="side-menu">
      <li><svg class="arrow" viewBox="0 0 21 21"><circle cx="10.5" cy="10.5" r="9" fill="#eee" stroke="#888"/><path d="M8.5 6.5 13 10.5 8.5 14.5z" fill="#555"/></svg>Accounting &amp; Financials</li>
      <li><svg class="arrow" viewBox="0 0 21 21"><circle cx="10.5" cy="10.5" r="9" fill="#eee" stroke="#888"/><path d="M8.5 6.5 13 10.5 8.5 14.5z" fill="#555"/></svg>Distribution</li>
      <li><svg class="arrow" viewBox="0 0 21 21"><circle cx="10.5" cy="10.5" r="9" fill="#eee" stroke="#888"/><path d="M8.5 6.5 13 10.5 8.5 14.5z" fill="#555"/></svg>Financial Services</li>
      <li><svg class="arrow" viewBox="0 0 21 21"><circle cx="10.5" cy="10.5" r="9" fill="#eee" stroke="#888"/><path d="M8.5 6.5 13 10.5 8.5 14.5z" fill="#555"/></svg>Food and Beverage</li>
      <li><svg class="arrow" viewBox="0 0 21 21"><circle cx="10.5" cy="10.5" r="9" fill="#eee" stroke="#888"/><path d="M8.5 6.5 13 10.5 8.5 14.5z" fill="#555"/></svg>Mining-Resource</li>
      <li><svg class="arrow" viewBox="0 0 21 21"><circle cx="10.5" cy="10.5" r="9" fill="#eee" stroke="#888"/><path d="M8.5 6.5 13 10.5 8.5 14.5z" fill="#555"/></svg>Process Manufacturing</li>
      <li><svg class="arrow" viewBox="0 0 21 21"><circle cx="10.5" cy="10.5" r="9" fill="#eee" stroke="#888"/><path d="M8.5 6.5 13 10.5 8.5 14.5z" fill="#555"/></svg>Project Time Accounting</li>
      <li><svg class="arrow" viewBox="0 0 21 21"><circle cx="10.5" cy="10.5" r="9" fill="#eee" stroke="#888"/><path d="M8.5 6.5 13 10.5 8.5 14.5z" fill="#555"/></svg>Services Management</li>
      <li><svg class="arrow" viewBox="0 0 21 21"><circle cx="10.5" cy="10.5" r="9" fill="#eee" stroke="#888"/><path d="M8.5 6.5 13 10.5 8.5 14.5z" fill="#555"/></svg>Textiles &amp; Fashion</li>
    </ul>
    <div class="side-link remote"><span class="icon" role="img" aria-label="Illustration of a support figure with an arrow"></span>Remote Support</div>
    <div class="side-link cases"><span class="icon" role="img" aria-label="Illustration of a briefcase"></span>Case Studies</div>
  </aside>

  <h2 class="content-title">Industries Served</h2>

  <article class="card c1">
    <h3>Accounting and Financials</h3>
    <p>Accounting &amp; Financials<br>Escape the tyranny of Gridwell<br>spreadsheets as your primary<br>management reporting<br>mechanism....</p>
    <div class="thumb" role="img" aria-label="Picture of a stack of banknotes beside a calculator"></div>
  </article>
  <article class="card c2">
    <h3>Distribution</h3>
    <p>Distribution We can help you:<br>Reduce your required<br>inventory levels, and improve<br>your inventory turnover. Free<br>up....</p>
    <div class="thumb" role="img" aria-label="Picture of a cardboard shipping box with a red curved arrow"></div>
  </article>
  <article class="card c3">
    <h3>Financial Services</h3>
    <p>Accounting &amp; Financials<br>Escape the tyranny of Gridwell<br>spreadsheets as your primary<br>management reporting<br>mechanism....</p>
    <div class="thumb" role="img" aria-label="Picture of a banded bundle of dollar bills"></div>
  </article>
  <article class="card c4">
    <h3>Food and Beverage</h3>
    <p>Accounting &amp; Financials<br>Escape the tyranny of Gridwell<br>spreadsheets as your primary<br>management reporting<br>mechanism....</p>
    <div class="thumb" role="img" aria-label="Picture of a water bottle, a red apple and a sandwich"></div>
  </article>

</div>
</body>
</html>
```